Corvath Staffing Solutions - Magazine Ad

Local magazine ad for Corvath Staffing Solutions.
We are targeting local businesses, namely hospitality clients in the local Laguna Beach, CA area. This is an upscale, rather fancy, area so the target audience will be of a more professional sense. We want this advertisement to stand out from the rest. Feel free to use beach and other Laguna Beach, CA pics.
We want to provide the following contact info, clearly visible to direct traffic.
Contact info:
Dana Whitcombe
dwhitcombe@Brisdel.example
949-382-0465
Should include the text:
"Servicing:
- Professional
- Clerical
- Hospitality
- FInancial
- Highly Skilled Industrial"
Please include: www.Brisdel.example
This will be a full page ad.

```html
<!DOCTYPE html>
<html lang="en">
<head>
<meta charset="utf-8">
<title>Corvath Staffing Solutions – Magazine Ad</title>
<link rel="stylesheet" href="https://fonts.googleapis.com/css2?family=Allura&family=Montserrat:wght@400&display=swap">
<style>
  :root {
    --ink: #141414;
    --accent-blue: #3a78c2;
    --paper: #ffffff;
    --navy: #1f2f7a;
    --sea-blue: #3d63b8;
    --page-white: #f7f7f5;
    --aqua: #7fd2e6;
    --aqua-deep: #56bfd9;
    --sand: #e6cf86;
  }
  * { margin: 0; padding: 0; box-sizing: border-box; }
  html, body { width: 848px; height: 1200px; overflow: hidden; background: var(--paper); }
  .ad {
    position: relative;
    width: 848px;
    height: 1200px;
    overflow: hidden;
  }
  .beach-scene {
    position: absolute;
    inset: 0;
    background:
      radial-gradient(ellipse 260px 240px at 790px 110px, var(--sand) 0%, rgba(230,207,134,0) 100%),
      linear-gradient(118deg, var(--navy) 0%, var(--sea-blue) 20%, var(--page-white) 36%, var(--page-white) 68%, var(--aqua) 86%, var(--aqua-deep) 100%);
  }
  .corner-panel {
    position: absolute;
    inset: 0;
    width: 848px;
    height: 1200px;
  }
  .notes {
    position: absolute;
    left: 452px;
    top: 330px;
    transform: rotate(26deg);
    transform-origin: 0 42px;
    font-family: "Allura", cursive;
    color: var(--ink);
    white-space: nowrap;
  }
  .notes__title {
    font-size: 68px;
    line-height: 84px;
    font-weight: 400;
  }
  .notes__item {
    position: absolute;
    font-size: 44px;
    line-height: 1;
  }
  .contact {
    position: absolute;
    left: 156px;
    top: 774px;
    transform: rotate(25deg);
    transform-origin: 0 34px;
    font-family: "Allura", cursive;
    font-style: normal;
    color: var(--accent-blue);
    white-space: nowrap;
  }
  .contact__name {
    display: block;
    margin-left: 160px;
    font-size: 32px;
    line-height: 34px;
  }
  .contact__line {
    display: block;
    font-size: 28px;
    line-height: 34px;
  }
  .contact__divider {
    display: inline-block;
    width: 1px;
    height: 28px;
    margin: 0 10px;
    background: var(--accent-blue);
    vertical-align: middle;
  }
  .brand {
    position: absolute;
    left: 50px;
    top: 1096px;
    display: flex;
    align-items: center;
    gap: 10px;
    font-family: "Montserrat", sans-serif;
    font-weight: 400;
    color: var(--accent-blue);
    text-transform: uppercase;
    letter-spacing: 3px;
    font-size: 15px;
    line-height: 20px;
  }
  .brand__mark {
    width: 14px;
    height: 14px;
    background: var(--accent-blue);
    flex: none;
  }
  .website {
    position: absolute;
    left: 74px;
    top: 1150px;
    font-family: "Montserrat", sans-serif;
    font-weight: 400;
    font-size: 13px;
    letter-spacing: 1px;
    color: var(--accent-blue);
  }
</style>
</head>
<body>
  <main class="ad">
    <div class="beach-scene" role="img" aria-label="Photo of a striped beach towel with starfish, seashells and a straw bag, with an open spiral notebook lying on top"></div>

    <svg class="corner-panel" viewBox="0 0 848 1200" aria-hidden="true">
      <polygon points="0,716 424,1200 0,1200" fill="var(--paper)"/>
    </svg>

    <section class="notes" aria-label="Services">
      <h1 class="notes__title">Servicing:</h1>
      <p class="notes__item" style="left:60px; top:100px;">- Professional</p>
      <p class="notes__item" style="left:42px; top:172px;">- Clerical</p>
      <p class="notes__item" style="left:46px; top:244px;">- Hospitality</p>
      <p class="notes__item" style="left:46px; top:316px;">- Financial</p>
      <p class="notes__item" style="left:50px; top:382px;">- Highly Skilled<br>Industrial</p>
    </section>

    <address class="contact">
      <span class="contact__name">Dana Whitcombe</span>
      <span class="contact__line">dwhitcombe@Brisdel.example<span class="contact__divider"></span>949-382-0465</span>
    </address>

    <div class="brand">
      <span class="brand__mark"></span>
      <span class="brand__name">Corvath<br>Staffing Solutions</span>
    </div>
    <p class="website">www.Brisdel.example</p>
  </main>
</body>
</html>
```